Updates

Please take these words out of the flyer " or any other fees whatsoever." Added Monday, August 8, 2016

Industry/Entity Type

Real Estate

Font styles to use
Serif

Requirements
Must have

```html
<!DOCTYPE html>
<html lang="en">
<head>
<meta charset="utf-8">
<title>Summit Keystone Realty – Commission Plans Flyer</title>
<link href="https://fonts.googleapis.com/css2?family=Montserrat:wght@700;800&family=Mulish:wght@600;700;800&family=Crimson+Text:wght@600;700&display=swap" rel="stylesheet">
<style>
  :root {
    --brand-red: #e8222b;
    --ink-dark: #262626;
    --panel-grey: #8c8c8c;
    --paper: #ffffff;
    --backdrop: #d9d9d9;
    --text-grey: #4a4a4a;
    --rule-grey: #bdbdbd;
    --photo-house-top: #6f86a6;
    --photo-house-mid: #b59a78;
    --photo-house-low: #4f7a3a;
    --photo-pool-sky: #9cc7e4;
    --photo-pool-water: #2fb3d6;
    --photo-pool-palm: #3f6b3a;
  }
  * { box-sizing: border-box; margin: 0; padding: 0; }
  html, body { width: 1200px; height: 944px; overflow: hidden; }
  body {
    background: var(--backdrop);
    font-family: "Mulish", Arial, sans-serif;
    position: relative;
  }
  .flyer {
    position: absolute; left: 282px; top: 22px;
    width: 636px; height: 900px;
    background: var(--paper);
    overflow: hidden;
  }
  .flyer > * { position: absolute; }

  /* header */
  .brand-box {
    left: 0; top: 0; width: 270px; height: 150px;
    display: flex; align-items: center; justify-content: center; gap: 10px;
  }
  .brand-mark { width: 16px; height: 16px; background: var(--brand-red); flex: none; }
  .brand-name { color: var(--brand-red); font-weight: 700; font-size: 19px; white-space: nowrap; }
  .headline-box {
    left: 270px; top: 0; width: 366px; height: 150px;
    background: var(--brand-red); color: var(--paper);
    padding: 34px 0 0 24px;
  }
  .headline-lead { font-family: "Montserrat", sans-serif; font-weight: 800; font-size: 34px; line-height: 1; color: var(--ink-dark); }
  .headline-sub { font-family: "Montserrat", sans-serif; font-weight: 700; font-size: 26px; margin-top: 6px; padding-bottom: 8px; border-bottom: 2px solid var(--paper); width: 330px; white-space: nowrap; }

  /* plan panel */
  .plans-panel { left: 0; top: 150px; width: 270px; height: 340px; background: var(--panel-grey); }
  .plan-ribbon {
    position: absolute; left: 0; width: 258px; height: 40px;
    background: var(--ink-dark);
    clip-path: polygon(0 0, 100% 0, 94% 50%, 100% 100%, 0 100%, 6% 50%);
    display: flex; align-items: center; justify-content: center; gap: 8px;
    font-family: "Crimson Text", serif; font-size: 24px; font-weight: 600;
  }
  .ribbon-num { color: var(--paper); }
  .ribbon-word { color: var(--brand-red); font-weight: 700; }
  .plan-text {
    position: absolute; left: 24px; width: 236px;
    color: var(--paper); font-weight: 700; font-size: 19px; line-height: 1.2;
  }
  .price-sign { color: var(--brand-red); }
  .plan-one-ribbon { top: 24px; }
  .plan-one-text { top: 76px; }
  .plan-two-ribbon { top: 196px; }
  .plan-two-text { top: 250px; }

  /* photos */
  .photo-house {
    left: 282px; top: 160px; width: 342px; height: 262px;
    background: linear-gradient(180deg, var(--photo-house-top) 0%, var(--photo-house-mid) 55%, var(--photo-house-low) 100%);
  }
  .photo-pool {
    left: 0; top: 490px; width: 270px; height: 200px;
    background: linear-gradient(180deg, var(--photo-pool-sky) 0%, var(--photo-pool-palm) 50%, var(--photo-pool-water) 100%);
  }

  /* third plan */
  .plan-three-box {
    left: 270px; top: 432px; width: 366px; height: 268px;
    background: var(--brand-red);
  }
  .plan-three-box .plan-ribbon { left: 42px; top: 42px; width: 282px; }
  .plan-three-text {
    position: absolute; left: 28px; top: 110px; width: 310px;
    color: var(--paper); font-weight: 700; font-size: 20px; line-height: 1.2; text-align: center;
  }

  /* contact */
  .contact-person { left: 26px; top: 722px; width: 220px; }
  .person-name { color: var(--brand-red); font-weight: 800; font-size: 19px; white-space: nowrap; }
  .person-role { color: var(--text-grey); font-weight: 700; font-size: 15px; margin-top: 2px; }
  .person-phone { font-family: "Montserrat", sans-serif; color: var(--ink-dark); font-weight: 800; font-size: 24px; margin-top: 6px; white-space: nowrap; }
  .contact-divider { left: 262px; top: 722px; width: 1px; height: 100px; background: var(--rule-grey); }
  .contact-details { left: 282px; top: 726px; width: 350px; color: var(--ink-dark); }
  .detail-row { font-weight: 700; font-size: 17px; margin-bottom: 6px; white-space: nowrap; }
  .detail-label { color: var(--brand-red); font-weight: 800; margin-right: 10px; }
  .detail-address { font-size: 11.5px; font-weight: 600; white-space: nowrap; }

  .web-band {
    left: 0; top: 846px; width: 636px; height: 54px;
    background: var(--brand-red); color: var(--paper);
    display: flex; align-items: center; justify-content: center;
    font-family: "Montserrat", sans-serif; font-weight: 700; font-size: 18px; letter-spacing: 9px;
  }
</style>
</head>
<body>
  <article class="flyer">
    <div class="brand-box">
      <span class="brand-mark"></span>
      <span class="brand-name">Summit Keystone Realty</span>
    </div>
    <header class="headline-box">
      <h1 class="headline-lead">WE HAVE</h1>
      <p class="headline-sub">3 commission plans</p>
    </header>

    <section class="plans-panel">
      <div class="plan-ribbon plan-one-ribbon"><span class="ribbon-num">1st</span><span class="ribbon-word">PLAN</span></div>
      <p class="plan-text plan-one-text">100% commission<br>99 dollars a month<br>and <span class="price-sign">$</span>249 per<br>transaction.</p>
      <div class="plan-ribbon plan-two-ribbon"><span class="ribbon-num">2nd</span><span class="ribbon-word">PLAN</span></div>
      <p class="plan-text plan-two-text">90/10 for<br><span class="price-sign">$</span>69 per month.</p>
    </section>

    <div class="photo-house" role="img" aria-label="Photo of a two-storey family house at dusk with lit windows and lawn"></div>
    <div class="photo-pool" role="img" aria-label="Photo of a resort building with palm trees and a swimming pool"></div>

    <section class="plan-three-box">
      <div class="plan-ribbon"><span class="ribbon-num">3rd</span><span class="ribbon-word">PLAN</span></div>
      <p class="plan-three-text">80/20 all plans have no office fees, no franchise fees.</p>
    </section>

    <div class="contact-person">
      <p class="person-name">Marisa Kolvenko</p>
      <p class="person-role">Broker Owner</p>
      <p class="person-phone">555-304-7718</p>
    </div>
    <div class="contact-divider"></div>
    <div class="contact-details">
      <p class="detail-row"><span class="detail-label">Email:</span>lorem@loremipsum.com</p>
      <p class="detail-row"><span class="detail-label">FAX:</span>123 456 7890</p>
      <p class="detail-address">4820 Ridgeline Ave, Arlington, TX 75010 1st floor 210</p>
    </div>

    <footer class="web-band">www.lorem.com</footer>
  </article>
</body>
</html>
```